We are a small business - Tree Care Company owned bt a certified Arborist. We would like an advertis

Hurricane season is approaching. We would like our current and potential customers to hire us for their tree work - safety first.

A little bit about us:

We are OKV-certified and insured, you can be confident that you will be able to trust us on your property. We maintain a clean, organized, and safe working environment.

Our tree service services St Petersburg, Clearwater, Belleair, Seminole, and surrounding tampa bay areas cover anything and everything that you may find yourself needing regarding tree care services.

Some of our specialties include tree pruning and trimming, removal, support, planting, emergency tree service, and much, much more.

For hurricane prep, make sure your trees are properly maintained and inspected for structual issues.

Target Market(s)

late 20's to 65. Homeow

Requirements
Must have
• A Call to action. Call us to schedule a FREE estimate.
• 1-866-540-GLOBE

```html
<!DOCTYPE html>
<html lang="en">
<head>
<meta charset="utf-8">
<title>Canopywise Professional Tree Care Flyer</title>
<link href="https://fonts.googleapis.com/css2?family=Oswald:wght@400;500;600&family=Open+Sans:wght@400;600;700&display=swap" rel="stylesheet">
<style>
  :root{
    --green:#6cb33f;
    --green-dark:#4a8a26;
    --green-light:#8cc63f;
    --ink:#333333;
    --footer:#3b3b3b;
    --white:#ffffff;
    --paper:#ffffff;
  }
  *{box-sizing:border-box;margin:0;padding:0}
  html,body{width:707px;height:1200px;overflow:hidden;background:var(--paper)}
  body{font-family:"Open Sans",Arial,sans-serif;color:var(--ink)}
  .flyer{position:relative;width:707px;height:1200px;background:var(--paper)}

  .brand{position:absolute;left:0;top:0;width:707px;height:210px;display:flex;flex-direction:column;align-items:center;justify-content:center;gap:8px}
  .brand-row{display:flex;align-items:center;gap:14px}
  .brand-dot{width:30px;height:30px;border-radius:50%;background:var(--green)}
  .brand-name{font-family:"Oswald",Arial,sans-serif;font-weight:500;font-size:66px;line-height:1;color:var(--green)}
  .brand-tag{font-family:"Oswald",Arial,sans-serif;font-size:22px;letter-spacing:6px;color:var(--green);text-transform:uppercase}

  .photo{position:absolute}
  .photo-tree{left:28px;top:220px;width:318px;height:312px;background:linear-gradient(180deg,#9cc3e6 0%,#6f8f5a 45%,#3e5a2c 80%,#7d7f6a 100%)}
  .photo-palms{left:362px;top:470px;width:317px;height:250px;background:linear-gradient(180deg,#a9cdeb 0%,#79986a 50%,#55683f 75%,#9a9a92 100%)}
  .photo-grinder{left:28px;top:690px;width:318px;height:350px;background:linear-gradient(160deg,#4f6b34 0%,#7a7a42 40%,#c99a1e 65%,#5b4a2a 100%)}

  .about{position:absolute;left:362px;top:220px;width:317px;height:240px;background:var(--green);color:var(--white);padding:22px 24px}
  .section-title{font-family:"Oswald",Arial,sans-serif;font-weight:500;font-size:34px;line-height:1;text-transform:uppercase;letter-spacing:1px}
  .about p{margin-top:16px;font-size:15px;line-height:1.55}

  .heading-band{position:absolute;height:58px;background:var(--green-dark);color:var(--white);display:flex;align-items:center;padding:0 22px}
  .heading-areas{left:28px;top:546px;width:318px}
  .heading-specialties{left:362px;top:734px;width:317px}

  .areas-text{position:absolute;left:28px;top:604px;width:318px;height:76px;background:var(--green);color:var(--white);padding:12px 22px;font-size:14px;line-height:1.5}

  .specialties{position:absolute;left:362px;top:792px;width:317px;height:248px;background:linear-gradient(135deg,#5e9d33 0%,#7fbd45 50%,#3f7a22 100%);padding:16px 22px}
  .specialties ul{list-style:none}
  .specialties li{display:flex;align-items:center;gap:10px;color:var(--white);font-size:15px;font-weight:600;line-height:1.2;margin-bottom:9px}
  .specialties svg{flex:none}

  .footer{position:absolute;left:0;top:1058px;width:707px;height:142px;background:var(--footer);border-top:6px solid var(--green);padding:20px 28px;display:flex;justify-content:space-between;align-items:center}
  .cta-line{font-family:"Oswald",Arial,sans-serif;font-size:26px;color:var(--white)}
  .cta-line strong{color:var(--green-light);font-weight:600}
  .phone{font-family:"Oswald",Arial,sans-serif;font-weight:600;font-size:40px;color:var(--green-light);line-height:1.1;margin-top:4px}
  .web{font-size:13px;color:#d8d8d8;margin-top:4px}
  .badges{display:flex;gap:12px;align-items:center}
  .badge{width:52px;height:52px;background:#e6e6e6}
  .badge.round{border-radius:50%}
</style>
</head>
<body>
<main class="flyer">
  <header class="brand">
    <div class="brand-row">
      <span class="brand-dot"></span>
      <span class="brand-name">Canopywise</span>
    </div>
    <div class="brand-tag">Professional Tree Care</div>
  </header>

  <div class="photo photo-tree" role="img" aria-label="Photo of a large oak tree beside a house"></div>

  <section class="about">
    <h2 class="section-title">About Us</h2>
    <p>As OKV-certified and insured tree professionals, we keep every job clean, organized and safe, so you can trust us on your property all year round.</p>
  </section>

  <div class="photo photo-palms" role="img" aria-label="Photo of palm trees with work trucks parked on a street"></div>

  <div class="heading-band heading-areas"><h2 class="section-title">Areas We Service</h2></div>
  <p class="areas-text">We service St Petersburg, Clearwater, Belleair, Seminole and the surrounding Tampa Bay areas.</p>

  <div class="photo photo-grinder" role="img" aria-label="Photo of a yellow stump grinder at work on a lawn"></div>

  <div class="heading-band heading-specialties"><h2 class="section-title">Our Specialties</h2></div>
  <section class="specialties" aria-label="Our specialties">
    <ul>
      <li><svg width="16" height="16" viewBox="0 0 16 16"><path d="M2 8l4 4 8-9" fill="none" stroke="#fff" stroke-width="2.5"/></svg>Hurricane Preparation</li>
      <li><svg width="16" height="16" viewBox="0 0 16 16"><path d="M2 8l4 4 8-9" fill="none" stroke="#fff" stroke-width="2.5"/></svg>Tree Pruning</li>
      <li><svg width="16" height="16" viewBox="0 0 16 16"><path d="M2 8l4 4 8-9" fill="none" stroke="#fff" stroke-width="2.5"/></svg>Trimming</li>
      <li><svg width="16" height="16" viewBox="0 0 16 16"><path d="M2 8l4 4 8-9" fill="none" stroke="#fff" stroke-width="2.5"/></svg>Removal</li>
      <li><svg width="16" height="16" viewBox="0 0 16 16"><path d="M2 8l4 4 8-9" fill="none" stroke="#fff" stroke-width="2.5"/></svg>Support</li>
      <li><svg width="16" height="16" viewBox="0 0 16 16"><path d="M2 8l4 4 8-9" fill="none" stroke="#fff" stroke-width="2.5"/></svg>Planting</li>
      <li><svg width="16" height="16" viewBox="0 0 16 16"><path d="M2 8l4 4 8-9" fill="none" stroke="#fff" stroke-width="2.5"/></svg>Emergency tree service and much more</li>
    </ul>
  </section>

  <footer class="footer">
    <div class="cta">
      <div class="cta-line">Call us to schedule a <strong>FREE</strong> estimate</div>
      <div class="phone">1-866-540-GLOBE</div>
      <div class="web">www.canopywisetrees.com</div>
    </div>
    <div class="badges">
      <span class="badge round"></span>
      <span class="badge"></span>
      <span class="badge round"></span>
    </div>
  </footer>
</main>
</body>
</html>
```